Hotdogs & Burgers restaurant needs a new menu design

We need a new menu design for our restaurant "Wurmelo". Wurmelo is a fast food specialized in hotdogs and burgers.We are looking for a simple easy menu design that walk through our customer to order the sandwich ==> the fries =>> the sides and the drinks. Wurmelo Menu:* Sandwiches**Hotdogs Our special fresh grilled hotdog served on fresh buns (Regular – 1.300 OMR / Franks – 2.000 OMR)*** DoganzaLettuce, tomato, jalapeno, pickle, onion, corn, chips, cheese, ketchup, mayo, mustard*** PepperBell pepper, onion, sweet chili sauce, avocado*** Chili FlamesChili carne, cheddar cheese, honey mustard*** ChicagoTomato, pickle, red onion, sweet relish, mustard*** New YorkGrilled onion, beef bacon, barbecue sauce, chili mustard*** Egg & CheeseOmelet, cheese, ketchup, mayo, mustard** Burgers 100% all natural beef & freshly ground, 100 grams each patty served on fresh buns.(Single patty - 2.000 OMR / double patty - 2.500 OMR)*** Sweet Beef BurgerBeef bacon, cheese, lettuce, tomato, pickle.*** Cheese Beef BurgerCheese, pickle, Wurmelo sauce.*** Mexican Beef BurgerGuacamole sauce, red onion, lettuce, tomato, Wurmelo sauce.*** Chicken BurgerFried chicken patty, lettuce, tomato, ranch sauce, Wurmelo sauce== ToppingsExtra veggies 0.100 OMRExtra cheese 0.200 OMRExtra beef Bacon 0.400 OMRExtra patty 0.500 OMR*Fries**Regular 0.600 OMR**Crispy 0.800 OMR**Wedges 0.800 OMR**Chili fries 1.500 OMRTopped with our chili carne, cheddar cheese, jalapeno, honey mustard**Lava fries 1.500 OMRTopped with fried bacon, fried onion, cheddar cheese, ranch sauce*Sides**Crispy strips 1.800 OMR5 pieces of chicken strips topped with BBQ sauce or honey mustard sauce, Wurmelo side sauce**Jalapeno cheese balls 1.300 OMR6 pieces of jalapeno cheese balls, sweet chili side sauce**Nachos 1.500 OMRA plate of nachos topped with cheddar cheese and jalapeno*Drinks**Flavored sparkling cans 0.800 OMR **Fresh orange juice 1.400 OMR**Mineral water 0.300 OMR**Soft drink 0.400 OMR**Mojito 1.500 OMRThe menu should not have any of our products pictures (icons/symbols proffered). we would prefer if the designs have unique icons/symbols created for Wurmelo. you can check our Instagram page https://www.snapfolio.example/wurmelo.official/

Industry/Entity Type

American Restaurant

Colors

Designer to choose colors to be used in the design.

Requirements
Must have
• Wurmelo Logo, Icons

```html
<!DOCTYPE html>
<html lang="en">
<head>
<meta charset="utf-8">
<title>Wurmelo Menu</title>
<link href="https://fonts.googleapis.com/css2?family=Patrick+Hand+SC&family=Gochi+Hand&display=swap" rel="stylesheet">
<style>
  :root {
    --bg-dark: #141414;
    --bg-mid: #343434;
    --yellow: #f7e11c;
    --red: #d6171d;
    --white: #f2f2f2;
    --badge-edge: #5a5a5a;
    --badge-fill: #1c1c1c;
  }
  html, body { margin: 0; padding: 0; overflow: hidden; }
  .menu {
    position: relative;
    width: 1200px;
    height: 859px;
    overflow: hidden;
    background: radial-gradient(ellipse at 50% 45%, var(--bg-mid) 0%, #222 55%, var(--bg-dark) 100%);
    font-family: "Patrick Hand SC", cursive;
    color: var(--white);
    text-transform: uppercase;
  }
  .abs { position: absolute; margin: 0; line-height: 1; white-space: nowrap; }
  .yellow { color: var(--yellow); }
  .red { color: var(--red); }
  .section-title { font-size: 50px; letter-spacing: 1px; }
  .sub-title { font-size: 46px; }
  .item-name { font-size: 25px; color: var(--yellow); }
  .item-desc { font-size: 14px; color: var(--white); line-height: 1.3; }
  .price { font-family: "Gochi Hand", cursive; color: var(--white); font-size: 30px; text-align: right; }
  .price-sm { font-family: "Gochi Hand", cursive; color: var(--white); font-size: 21px; text-align: right; }

  .badge {
    position: absolute;
    border-radius: 50%;
    background: radial-gradient(circle at 50% 35%, #3a3a3a, var(--badge-fill) 70%);
    border: 2px solid var(--badge-edge);
    box-shadow: 0 3px 6px rgba(0,0,0,.6);
    display: flex; flex-direction: column; align-items: center; justify-content: center;
    color: var(--yellow);
    text-align: center;
    line-height: 1.15;
  }
  .badge .label { font-size: 15px; }
  .badge .amount { font-family: "Gochi Hand", cursive; font-size: 18px; }
  .price-badge { width: 92px; height: 92px; }
  .icon-badge { width: 84px; height: 84px; }
  .icon-art { width: 50px; height: 40px; border-radius: 40%; }
  .icon-art.yellow-art { background: radial-gradient(circle, #f7e11c, #c9b012); }
  .icon-art.red-art { background: radial-gradient(circle, #e3282d, #a81015); }

  .brand-disc {
    position: absolute; left: 484px; top: 302px; width: 252px; height: 252px;
    border-radius: 50%;
    background: radial-gradient(circle at 50% 40%, #2c2c2c, #0c0c0c 75%);
    box-shadow: 0 0 14px rgba(0,0,0,.8);
  }
  .brand-name { left: 0; right: 0; top: 88px; text-align: center; font-size: 52px; color: var(--yellow); }
  .brand-menu { left: 0; right: 0; top: 146px; text-align: center; font-size: 78px; color: var(--red); }

  .toppings-rule { position: absolute; left: 216px; top: 548px; width: 3px; height: 272px; background: var(--red); }
  .right { text-align: right; }
</style>
</head>
<body>
<main class="menu">

  <!-- Sandwiches / Hotdogs -->
  <h1 class="abs section-title yellow" style="left:214px;top:36px;">Sandwiches</h1>
  <div class="badge icon-badge" style="left:26px;top:186px;"><div class="icon-art yellow-art" role="img" aria-label="Hotdog icon"></div></div>
  <h2 class="abs sub-title red" style="left:88px;top:108px;font-size:50px;">Hotdogs</h2>
  <p class="abs item-desc" style="left:292px;top:114px;font-size:16px;">Our special fresh grilled<br>hotdog served on fresh buns</p>
  <div class="badge price-badge" style="left:548px;top:84px;"><span class="label">Regular</span><span class="amount">1.300 OMR</span></div>
  <div class="badge price-badge" style="left:550px;top:186px;"><span class="label">Franks</span><span class="amount">2.000 OMR</span></div>

  <section class="hotdog-list">
    <p class="abs item-name right" style="right:972px;top:172px;">Wurmelo</p>
    <p class="abs item-desc" style="left:240px;top:168px;">Lettuce, tomato, jalapeno, pickle, onion,<br>corn, chips, cheese, ketchup, mayo, mustard</p>
    <p class="abs item-name right" style="right:982px;top:204px;">Pepper</p>
    <p class="abs item-desc" style="left:237px;top:210px;">Bell pepper, onion, sweet chili sauce, avocado</p>
    <p class="abs item-name right" style="right:950px;top:230px;">Chili Flames</p>
    <p class="abs item-desc" style="left:263px;top:237px;">Chili carne, cheddar cheese, honey mustard</p>
    <p class="abs item-name right" style="right:976px;top:258px;">Chicago</p>
    <p class="abs item-desc" style="left:238px;top:264px;">Tomato, pickle, red onion, sweet relish, mustard</p>
    <p class="abs item-name right" style="right:968px;top:284px;">New York</p>
    <p class="abs item-desc" style="left:243px;top:290px;">Grilled onion, beef bacon, barbecue sauce, chili mustard</p>
    <p class="abs item-name right" style="right:950px;top:311px;">Egg &amp; Cheese</p>
    <p class="abs item-desc" style="left:258px;top:316px;">Omelet, cheese, ketchup, mayo, mustard</p>
  </section>

  <!-- Burgers -->
  <div class="badge icon-badge" style="left:28px;top:372px;"><div class="icon-art red-art" role="img" aria-label="Burger icon"></div></div>
  <h2 class="abs sub-title yellow" style="left:132px;top:388px;font-size:52px;">Burgers</h2>
  <div class="badge price-badge" style="left:348px;top:348px;"><span class="label">Single patty</span><span class="amount">2.000 OMR</span></div>
  <div class="badge price-badge" style="left:350px;top:454px;"><span class="label">Double patty</span><span class="amount">2.500 OMR</span></div>
  <p class="abs item-desc right" style="right:884px;top:452px;font-size:16px;line-height:1.35;">100% all natural beef &amp;<br>freshly ground, 100 grams each<br>patty served on fresh buns.</p>

  <h3 class="abs red" style="left:64px;top:550px;font-size:28px;">Toppings</h3>
  <section class="toppings">
    <p class="abs item-name" style="left:32px;top:596px;">Extra veggies</p>
    <p class="abs price-sm" style="right:1004px;top:622px;">0.100 OMRE</p>
    <p class="abs item-name" style="left:42px;top:650px;">Extra cheese</p>
    <p class="abs price-sm" style="right:1004px;top:676px;">0.200 OMRE</p>
    <p class="abs item-name" style="left:20px;top:704px;">Extra beef bacon</p>
    <p class="abs price-sm" style="right:1004px;top:730px;">0.400 OMRE</p>
    <p class="abs item-name" style="left:44px;top:762px;">Extra patty</p>
    <p class="abs price-sm" style="right:1004px;top:788px;">0.500 OMRE</p>
  </section>
  <div class="toppings-rule"></div>

  <section class="burger-list">
    <p class="abs item-name" style="left:234px;top:556px;">Sweet Beef Burger</p>
    <p class="abs item-desc" style="left:244px;top:588px;">Beef bacon, cheese, lettuce, tomato, pickle.</p>
    <p class="abs item-name" style="left:234px;top:618px;">Cheese Beef Burger</p>
    <p class="abs item-desc" style="left:246px;top:648px;">Cheese, pickle, Wurmelo sauce</p>
    <p class="abs item-name" style="left:234px;top:676px;">Mexican Beef Burger</p>
    <p class="abs item-desc" style="left:246px;top:706px;">Guacamole sauce, red onion, lettuce,<br>tomato, Wurmelo sauce.</p>
    <p class="abs item-name" style="left:232px;top:754px;">Chicken Burger</p>
    <p class="abs item-desc" style="left:248px;top:786px;">Fried chicken patty, lettuce, tomato, ranch<br>sauce, Wurmelo sauce</p>
  </section>

  <!-- Brand centre -->
  <div class="brand-disc">
    <p class="abs brand-name">Wurmelo</p>
    <p class="abs brand-menu">Menu</p>
  </div>

  <!-- Fries -->
  <div class="badge icon-badge" style="left:702px;top:42px;"><div class="icon-art red-art" role="img" aria-label="Fries icon"></div></div>
  <h2 class="abs sub-title yellow" style="left:804px;top:60px;font-size:52px;">Fries</h2>
  <div class="badge price-badge" style="left:942px;top:36px;"><span class="label">Regular</span><span class="amount">0.600 OMR</span></div>
  <div class="badge price-badge" style="left:1052px;top:36px;"><span class="label">Crispy</span><span class="amount">0.800 OMR</span></div>

  <section class="fries-list">
    <p class="abs item-name" style="left:784px;top:148px;font-size:28px;">Wedges</p>
    <p class="abs price" style="right:74px;top:146px;">0.800 OMR</p>
    <p class="abs item-name" style="left:784px;top:182px;font-size:28px;">Chili Fries</p>
    <p class="abs price" style="right:74px;top:180px;">1.500 OMR</p>
    <p class="abs item-desc" style="left:806px;top:214px;">Topped with our chili carne, cheddar<br>cheese, jalapeno, honey mustard</p>
    <p class="abs item-name" style="left:786px;top:254px;font-size:28px;">Lava Fries</p>
    <p class="abs price" style="right:74px;top:252px;">1.500 OMR</p>
    <p class="abs item-desc" style="left:804px;top:286px;">Topped with fried bacon, fried onion,<br>cheddar cheese, ranch sauce</p>
  </section>

  <!-- Sides -->
  <div class="badge icon-badge" style="left:764px;top:340px;"><div class="icon-art yellow-art" role="img" aria-label="Sides icon"></div></div>
  <h2 class="abs sub-title red" style="left:864px;top:354px;font-size:54px;">Sides</h2>

  <section class="sides-list">
    <p class="abs item-name" style="left:798px;top:436px;font-size:29px;">Crispy Strips</p>
    <p class="abs price" style="right:26px;top:434px;font-size:32px;">1.800 OMR</p>
    <p class="abs item-desc" style="left:818px;top:470px;">5 pieces of chicken strips topped<br>with BBQ sauce or honey mustard<br>sauce, Wurmelo side sauce</p>
    <p class="abs item-name" style="left:700px;top:538px;font-size:31px;">Jalapeno Cheese Balls</p>
    <p class="abs price" style="right:26px;top:538px;font-size:32px;">1.300 OMR</p>
    <p class="abs item-desc" style="left:718px;top:576px;">6 pieces of jalapeno cheese balls,<br>sweet chili side sauce</p>
    <p class="abs item-name" style="left:706px;top:626px;font-size:31px;">Nachos</p>
    <p class="abs item-desc" style="left:808px;top:626px;">Plate of nachos topped with<br>cheddar cheese and jalapeno</p>
    <p class="abs price" style="right:26px;top:626px;font-size:32px;">1.500 OMR</p>
  </section>

  <!-- Drinks -->
  <h2 class="abs sub-title red" style="left:618px;top:722px;">Drinks</h2>
  <section class="drinks-list">
    <p class="abs item-name" style="left:776px;top:688px;">Flavored Sparkling Cans</p>
    <p class="abs price-sm" style="right:40px;top:688px;font-size:24px;">0.800 OMR</p>
    <p class="abs item-name" style="left:776px;top:720px;">Fresh Orange Juice</p>
    <p class="abs price-sm" style="right:40px;top:720px;font-size:24px;">1.400 OMR</p>
    <p class="abs item-name" style="left:776px;top:752px;">Mineral Water</p>
    <p class="abs price-sm" style="right:40px;top:750px;font-size:24px;">1.400 OMR</p>
    <p class="abs item-name" style="left:776px;top:782px;">Soft Drink</p>
    <p class="abs price-sm" style="right:40px;top:780px;font-size:24px;">0.400 OMR</p>
    <p class="abs item-name" style="left:776px;top:812px;">Mojito</p>
    <p class="abs price-sm" style="right:40px;top:810px;font-size:24px;">1.500 OMR</p>
  </section>

</main>
</body>
</html>
```